Qb Panes

We need a website design for a company based in Texas that specializes in doors and and windows.
Qb Pane is a leading window manufacturer of aluminum and vinyl windows, both serving the replacement and new construction markets. Qb Pane Inc. was created over 25 years ago when two existing window manufacturers with excellent reputations in their fields - merged. Qb Pane offers a complete line conforming to the needs of residential and commercial window markets.
The final design should be something that communicates professionalism and features they're key value propositions.
Example websites we like:
http://layouts.pebblecraft.example/zx/satchel/
http://layouts.pebblecraft.example/zx/splashyard/
http://layouts.pebblecraft.example/zx/rebuildr2/
This design should format the existing content to be more visually organized, improve the fonts to clearer and more readable, and make it easier for users to find services.
Brand guide is attached
Website images can be found here: https://docs.vaultcrate.example/7kRTmwQzLpXeBd
Target Market(s)
Windows
Number of Pages Required
1 page
Look and feel
Each slider illustrates characteristics of the customer's brand and the style your logo design should communicate.

```html
<!DOCTYPE html>
<html lang="en">
<head>
<meta charset="utf-8">
<title>Qb Pane — Windows &amp; Doors</title>
<link href="https://fonts.googleapis.com/css2?family=Montserrat:wght@400;500;600;700;800&family=Open+Sans:wght@400;600&display=swap" rel="stylesheet">
<style>
:root{
  --red:#9c1c33;
  --gold:#c9a43a;
  --ink:#2b2b2b;
  --muted:#777;
  --line:#e3e3e3;
  --white:#fff;
  --sky-top:#3f7fc4;
  --sky-low:#a9c9e6;
}
*{box-sizing:border-box;margin:0;padding:0}
html,body{width:1200px;height:3460px;overflow:hidden}
body{position:relative;font-family:"Open Sans",Arial,sans-serif;color:var(--ink);background:var(--white)}
.section-title{font-family:"Montserrat",Arial,sans-serif;font-weight:700;font-size:22px;letter-spacing:1px;text-align:center}
.section-title::after{content:"";display:block;width:40px;height:3px;background:var(--gold);margin:12px auto 0}

/* Hero */
.hero{position:absolute;left:0;top:0;width:1200px;height:640px;background:linear-gradient(180deg,var(--sky-top) 0%,var(--sky-low) 45%,#8a7a68 62%,#5c8a3c 82%,#4a7a30 100%)}
.topbar{position:absolute;left:0;top:0;width:1200px;height:100px}
.logo{position:absolute;left:120px;top:30px;display:flex;align-items:center;gap:10px;font-family:"Montserrat",Arial,sans-serif;font-weight:700;font-size:34px;color:var(--white)}
.logo .dot{width:14px;height:14px;border-radius:50%;background:var(--gold)}
.call{position:absolute;left:780px;top:14px;color:var(--white);font-family:"Montserrat",Arial,sans-serif;font-size:11px;line-height:16px}
.call b{display:block;font-size:17px;font-weight:600}
.btn-dealer{position:absolute;left:940px;top:18px;background:var(--red);color:var(--white);font:700 12px "Montserrat",Arial,sans-serif;padding:10px 18px;letter-spacing:.5px}
.menu{position:absolute;left:395px;top:64px;display:flex;gap:4px;font:600 11px "Montserrat",Arial,sans-serif;color:var(--white)}
.menu span{padding:8px 12px}
.menu .active{background:var(--white);color:var(--ink)}
.hero-photo{position:absolute;left:690px;top:140px;width:330px;height:500px;background:linear-gradient(180deg,#d9c2ad,#8f8a92 60%,#6e6f7a)}
.hero-tag{position:absolute;left:170px;top:290px;color:var(--white);font:500 24px "Montserrat",Arial,sans-serif}
.hero-head{position:absolute;left:170px;top:330px;color:var(--white);font:800 52px "Montserrat",Arial,sans-serif;letter-spacing:1px}
.dots{position:absolute;left:560px;top:615px;display:flex;gap:8px}
.dots i{width:8px;height:8px;border-radius:50%;background:rgba(255,255,255,.6)}
.dots i:first-child{background:var(--white)}

/* What we do */
.services-title{position:absolute;left:0;top:740px;width:1200px}
.service{position:absolute;top:860px;width:320px}
.service .ph{height:200px}
.service .label{position:relative;margin-top:18px;padding-left:20px;font:700 16px "Montserrat",Arial,sans-serif}
.service .label::before{content:"";position:absolute;left:0;top:-14px;width:14px;height:30px;border-left:3px solid var(--gold);border-bottom:3px solid var(--gold)}

/* Welcome */
.welcome{position:absolute;left:0;top:1240px;width:1200px;height:560px;background:linear-gradient(90deg,#fbfaf8 0%,#f4efe9 35%,#d9cfc3 60%,#b9a896 80%,#9b8a78 100%)}
.welcome-text{position:absolute;left:160px;top:130px;width:340px}
.welcome-text .rule{display:block;width:40px;height:3px;background:var(--gold)}
.welcome-text .kicker{font:600 16px "Montserrat",Arial,sans-serif;color:var(--gold);margin-top:16px}
.welcome-text h2{font:800 30px "Montserrat",Arial,sans-serif;color:var(--ink)}
.welcome-text p{font-size:12.5px;line-height:21px;color:#555;margin-top:16px}
.btn-red{display:inline-block;background:var(--red);color:var(--white);font:700 12px "Montserrat",Arial,sans-serif;padding:11px 20px;margin-top:24px}

/* Reviews */
.reviews{position:absolute;left:0;top:1800px;width:1200px;height:580px;background:#f6f6f6}
.reviews-photo{position:absolute;left:0;top:20px;width:300px;height:500px;background:linear-gradient(135deg,#cfd6db,#aeb8c0 50%,#8c97a0)}
.reviews .section-title{position:absolute;left:0;top:90px;width:1200px}
.review{position:absolute;top:210px;width:280px;height:260px;background:var(--white);box-shadow:0 2px 10px rgba(0,0,0,.08);padding:26px 24px}
.stars{color:var(--gold);font-size:15px;letter-spacing:2px;margin-left:24px}
.quote-mark{position:absolute;left:22px;top:18px;font:700 34px Georgia,serif;color:#ccc}
.review p{font-size:11.5px;line-height:19px;color:#666;margin-top:16px}
.reviewer{position:absolute;left:24px;bottom:26px;display:flex;align-items:center;gap:10px;font:600 10px "Montserrat",Arial,sans-serif}
.reviewer i{width:26px;height:26px;border-radius:50%;background:#b7b0a8}
.reviewer small{display:block;font-weight:400;color:var(--muted)}

/* Quote */
.quote{position:absolute;left:0;top:2390px;width:1200px;height:610px;background:linear-gradient(90deg,#8d8577 0%,#c9c1b4 30%,#e4ddd1 55%,#b88b4a 80%,#d3b07a 100%)}
.quote-panel{position:absolute;left:360px;top:20px;width:480px;height:580px;background:rgba(25,25,25,.88)}
.quote-vert{position:absolute;left:8px;top:80px;width:60px;height:420px;display:flex;align-items:center;justify-content:center}
.quote-vert span{transform:rotate(-90deg);white-space:nowrap;font:800 40px "Montserrat",Arial,sans-serif;color:rgba(255,255,255,.25);letter-spacing:4px}
.form{position:absolute;left:100px;top:40px;width:340px}
.field{height:32px;background:var(--white);margin-bottom:10px;font-size:11px;color:#888;padding:9px 10px}
.row{display:flex;gap:10px}
.row .field{flex:1}
.field.msg{height:90px}
.btn-gold{display:inline-block;background:var(--gold);color:var(--white);font:700 14px "Montserrat",Arial,sans-serif;padding:12px 36px;margin-top:6px}

/* Footer */
.footer{position:absolute;left:0;top:3000px;width:1200px;height:460px;background:var(--white)}
.fcol{position:absolute;top:60px;width:220px}
.fcol h4{font:700 11px "Montserrat",Arial,sans-serif;margin-bottom:12px}
.fcol li{list-style:none;font-size:11px;line-height:19px;color:#666}
.flogo{position:absolute;left:120px;top:250px;display:flex;align-items:center;gap:10px;font:700 34px "Montserrat",Arial,sans-serif;color:var(--red)}
.flogo .dot{width:14px;height:14px;border-radius:50%;background:var(--gold)}
.news{position:absolute;left:440px;top:240px}
.news h4{font:700 11px "Montserrat",Arial,sans-serif;margin-bottom:10px}
.news .box{display:flex}
.news .in{width:240px;height:34px;border:1px solid var(--line);font-size:11px;color:#999;padding:10px}
.news .go{background:var(--gold);color:var(--white);font:700 11px "Montserrat",Arial,sans-serif;padding:11px 20px}
.badge{position:absolute;top:250px;width:46px;height:46px}
.follow{position:absolute;left:120px;top:380px;display:flex;align-items:center;gap:8px;font:700 11px "Montserrat",Arial,sans-serif}
.follow i{width:22px;height:22px;border-radius:50%;background:#2f6fb3}
.copy{position:absolute;left:860px;top:384px;font-size:11px;color:var(--muted)}
.fline{position:absolute;left:120px;top:230px;width:960px;height:1px;background:var(--line)}
</style>
</head>
<body>

<header class="hero">
  <div class="hero-photo" role="img" aria-label="Smiling couple standing in front of a brick home with large windows"></div>
  <div class="topbar">
    <div class="logo"><span class="dot"></span>Qb Pane</div>
    <div class="call">CALL US<b>877-555-0142</b></div>
    <div class="btn-dealer">FIND A DEALER</div>
    <nav class="menu">
      <span class="active">HOME</span><span>OUR COMPANY</span><span>PERFORMANCE CENTER</span><span>WINDOWS</span><span>DOORS</span><span>SUNROOMS</span><span>CONTACT US</span>
    </nav>
  </div>
  <div class="hero-tag">Beautiful, Energy Efficient, Custom Windows &amp; Doors</div>
  <h1 class="hero-head">QB MAKES IT EASY</h1>
  <div class="dots"><i></i><i></i><i></i><i></i><i></i></div>
</header>

<section>
  <h2 class="section-title services-title">WHAT WE DO</h2>
  <div class="service" style="left:100px"><div class="ph" role="img" aria-label="Living room with wide windows" style="background:linear-gradient(135deg,#b98a5c,#d9c3a1 50%,#7fa6c4)"></div><div class="label">WINDOWS</div></div>
  <div class="service" style="left:440px"><div class="ph" role="img" aria-label="Glass patio doors at dusk" style="background:linear-gradient(135deg,#1f2c4a,#3c4d75 50%,#c79a5a)"></div><div class="label">DOORS</div></div>
  <div class="service" style="left:780px"><div class="ph" role="img" aria-label="Bright sun room with garden view" style="background:linear-gradient(135deg,#e8e2d4,#b8c9a3 50%,#6d8f4c)"></div><div class="label">SUN ROOMS</div></div>
</section>

<section class="welcome" role="img" aria-label="White kitchen with large windows">
  <div class="welcome-text">
    <span class="rule"></span>
    <div class="kicker">WELCOME TO</div>
    <h2>QB PANE</h2>
    <p>Qb Pane is proud that quality of product and quality of service are provided to build every home. Qb Pane is a leading window manufacturer of aluminum and vinyl windows, both serving the replacement and new construction markets. Qb Pane Inc. was created over 25 years ago when two existing window manufacturers merged.</p>
    <span class="btn-red">READ MORE</span>
  </div>
</section>

<section class="reviews">
  <div class="reviews-photo" role="img" aria-label="Happy senior couple at home"></div>
  <h2 class="section-title">PRODUCT REVIEWS</h2>
  <div class="review" style="left:140px"><span class="quote-mark">“</span><div class="stars">★★★★★</div><p>Our new windows keep the house cooler all summer long. The install team was quick, tidy and friendly, and the finish looks great from the street and inside every room.</p><div class="reviewer"><i></i><div>DALE MORROW<small>Customer</small></div></div></div>
  <div class="review" style="left:460px"><span class="quote-mark">“</span><div class="stars">★★★★★</div><p>We replaced every door and window in one week. Noise from the road is gone, our energy bill dropped, and the dealer answered each question with real care and patience.</p><div class="reviewer"><i></i><div>ANA REYES<small>Customer</small></div></div></div>
  <div class="review" style="left:780px"><span class="quote-mark">“</span><div class="stars">★★★★★</div><p>The sun room turned out better than we hoped. Clear glass, solid frames and a crew that kept us informed at every step. We would gladly choose them again for our next home.</p><div class="reviewer"><i></i><div>MARK ELLISON<small>Customer</small></div></div></div>
</section>

<section class="quote" role="img" aria-label="Open living room with patio windows">
  <div class="quote-panel">
    <div class="quote-vert"><span>GET A QUOTE</span></div>
    <div class="form">
      <div class="field">Name</div>
      <div class="field">Subject</div>
      <div class="field">E-mail</div>
      <div class="field">Phone</div>
      <div class="row"><div class="field">City</div><div class="field">State</div></div>
      <div class="field">Zipcode</div>
      <div class="field msg">Message</div>
      <span class="btn-gold">SUBMIT</span>
    </div>
  </div>
</section>

<footer class="footer">
  <div class="fcol" style="left:120px"><h4>ABOUT QB PANE</h4><ul><li>Press Releases</li><li>Our Community</li><li>Careers</li><li>Credentials &amp; Awards</li></ul></div>
  <div class="fcol" style="left:380px"><h4>OUR PRODUCTS</h4><ul><li>Vinyl Windows</li><li>Aluminum Windows</li><li>Doors</li><li>Patio Doors</li><li>Windows by Style</li><li>Locate a Dealer</li></ul></div>
  <div class="fcol" style="left:640px"><h4>LEARN ABOUT</h4><ul><li>Energy Savings</li><li>Replacement Windows</li><li>New Construction Windows</li><li>Knowledge Center</li></ul></div>
  <div class="fcol" style="left:900px"><h4>CONTACT US</h4><ul><li>Find a Dealer</li><li>Privacy Policy</li><li>Request Service</li></ul></div>
  <div class="fline"></div>
  <div class="flogo"><span class="dot"></span>Qb Pane</div>
  <div class="news"><h4>NEWSLETTER</h4><div class="box"><div class="in">E-mail</div><div class="go">SIGNUP</div></div></div>
  <div class="badge" style="left:960px;background:#2f6fb3"></div>
  <div class="badge" style="left:1020px;background:var(--red)"></div>
  <div class="follow">FOLLOW US<i></i><i></i><i style="background:#3b5998"></i><i style="background:#c0392b"></i><i style="background:#d35400"></i></div>
  <div class="copy">Copyright © 2016 All Rights Reserved</div>
</footer>

</body>
</html>
```